Velvet Harbor Entertainment Mobile djing services *

Please refer to the logo design uploaded and use the colors of my logo to the flyer design.

Id like a elegant and professional flyer to advertise my dj services for weddings and special events. I have different packages to choose from to cater to the need of the client. I offer custom gobos also.

Target Market(s)

Wedding

Industry/Entity Type

Entertainment Industry

Font styles to use
Script

Colors
000000

Requirements
Must have
• Fun pics reception, bride and groom dancing
Nice to have
• Professional, clean and eye catching design.

```html
<!DOCTYPE html>
<html lang="en">
<head>
<meta charset="utf-8">
<title>Velvet Harbor Entertainment – Flyer</title>
<link rel="stylesheet" href="https://fonts.googleapis.com/css2?family=Lobster&family=Montserrat:wght@400;600;700&display=swap">
<style>
  :root {
    --bg-top: #2a2a2a;
    --bg-bottom: #0c0c0c;
    --brand-red: #a3161c;
    --brand-black: #050505;
    --ink-white: #ffffff;
    --ink-soft: #e6e6e6;
  }
  * { box-sizing: border-box; margin: 0; padding: 0; }
  html, body { width: 1200px; height: 768px; overflow: hidden; }
  body {
    background: radial-gradient(ellipse at 50% 30%, var(--bg-top), var(--bg-bottom) 75%);
    font-family: "Montserrat", sans-serif;
    position: relative;
  }
  .flyer {
    position: absolute;
    top: 47px;
    width: 520px;
    height: 673px;
    overflow: hidden;
    background: var(--brand-black);
    box-shadow: 0 18px 40px rgba(0,0,0,.6);
  }
  .flyer--cover { left: 50px; }
  .flyer--packages { left: 630px; }
  .flyer__art { position: absolute; inset: 0; width: 100%; height: 100%; }

  .brand-name {
    position: absolute;
    font-family: "Montserrat", sans-serif;
    font-weight: 700;
    font-size: 19px;
    line-height: 1.15;
    letter-spacing: 2px;
    text-transform: uppercase;
    display: flex;
    align-items: center;
    gap: 8px;
  }
  .brand-name__dot { width: 14px; height: 14px; border-radius: 50%; flex: none; }
  .flyer--cover .brand-name { left: 34px; top: 330px; color: var(--brand-red); }
  .flyer--cover .brand-name__dot { background: var(--brand-red); }
  .flyer--packages .brand-name { right: 28px; top: 150px; color: var(--ink-white); text-align: right; }
  .flyer--packages .brand-name__dot { background: var(--ink-white); }

  .pill {
    position: absolute;
    background: var(--brand-red);
    color: var(--ink-white);
    font-family: "Lobster", cursive;
    font-weight: 400;
    border-radius: 20px;
    padding: 2px 18px 4px;
    white-space: nowrap;
    line-height: 1.2;
  }
  .pill--section { left: 0; top: 304px; font-size: 32px; padding: 4px 44px 6px 40px; border-radius: 0 28px 28px 0; }
  .pill--tier { font-size: 17px; }

  .package { position: absolute; width: 240px; }
  .package--silver { left: 64px; top: 372px; }
  .package--gold { left: 64px; top: 500px; }
  .package--platinum { left: 290px; top: 330px; }
  .package .pill { position: static; display: inline-block; margin-bottom: 5px; }
  .package__list {
    list-style: none;
    color: var(--ink-soft);
    font-size: 8.4px;
    line-height: 1.35;
  }
  .package__list li::before { content: "- "; }
  .package__list .sub { padding-left: 10px; }
  .package__list .sub::before { content: ""; }
  .package__price { color: var(--ink-white); font-weight: 700; font-size: 11px; margin-top: 2px; }

  .reservation {
    position: absolute;
    right: 18px;
    bottom: 38px;
    color: var(--ink-white);
    font-size: 10px;
    font-weight: 600;
    letter-spacing: .3px;
  }
</style>
</head>
<body>

<section class="flyer flyer--cover">
  <svg class="flyer__art" viewBox="0 0 520 673" preserveAspectRatio="none">
    <defs>
      <linearGradient id="bright-dance" x1="0" y1="0" x2="1" y2="1">
        <stop offset="0" stop-color="#f4f1f4"/>
        <stop offset=".5" stop-color="#cfc6cc"/>
        <stop offset="1" stop-color="#ece8ec"/>
      </linearGradient>
      <linearGradient id="warm-hall" x1="0" y1="0" x2="1" y2="1">
        <stop offset="0" stop-color="#2b1d12"/>
        <stop offset=".5" stop-color="#6b4a2c"/>
        <stop offset="1" stop-color="#c9c4c6"/>
      </linearGradient>
      <linearGradient id="dj-booth" x1="0" y1="0" x2="1" y2="1">
        <stop offset="0" stop-color="#3a2a6a"/>
        <stop offset=".5" stop-color="#5a3a8a"/>
        <stop offset="1" stop-color="#b0356e"/>
      </linearGradient>
    </defs>
    <rect role="img" aria-label="Photo: bride and groom sharing their first dance" width="520" height="673" fill="url(#warm-hall)"/>
    <path role="img" aria-label="Photo: wedding couple dancing under stage lights" d="M0 0 H520 V150 C420 200 380 300 300 360 C230 410 130 430 0 425 Z" fill="url(#bright-dance)"/>
    <path d="M0 425 C130 430 230 410 300 360 C380 300 420 200 520 150 V178 C440 220 400 320 320 385 C240 445 130 465 0 462 Z" fill="var(--brand-red)"/>
    <path d="M0 462 C130 465 240 445 320 385 C400 320 440 220 520 178 V190 C450 232 410 330 330 395 C250 458 130 478 0 476 Z" fill="var(--brand-black)"/>
    <path role="img" aria-label="Photo: DJ in a vest mixing on decks under purple lights" d="M0 600 C140 520 330 480 520 610 V673 H0 Z" fill="url(#dj-booth)"/>
    <path d="M0 600 C140 520 330 480 520 610 V640 C340 505 150 545 0 625 Z" fill="var(--brand-red)"/>
    <path d="M0 625 C150 545 340 505 520 640 V652 C340 520 150 560 0 638 Z" fill="var(--brand-black)"/>
  </svg>
  <div class="brand-name"><span class="brand-name__dot"></span><span>Velvet Harbor<br>Entertainment</span></div>
</section>

<section class="flyer flyer--packages">
  <svg class="flyer__art" viewBox="0 0 520 673" preserveAspectRatio="none">
    <defs>
      <linearGradient id="candle-kiss" x1="0" y1="0" x2="1" y2="1">
        <stop offset="0" stop-color="#3a2310"/>
        <stop offset=".45" stop-color="#a0703e"/>
        <stop offset="1" stop-color="#1e140c"/>
      </linearGradient>
    </defs>
    <path role="img" aria-label="Photo: bride and groom embracing in warm candlelight" d="M0 0 H520 V210 C360 290 180 255 0 300 Z" fill="url(#candle-kiss)"/>
    <path d="M0 300 C180 255 360 290 520 210 V232 C360 312 180 278 0 326 Z" fill="var(--brand-red)"/>
    <path d="M0 673 V662 C180 632 360 600 520 562 V574 C360 614 180 648 0 673 Z" fill="var(--brand-red)"/>
  </svg>

  <div class="brand-name"><span class="brand-name__dot"></span><span>Velvet Harbor<br>Entertainment</span></div>

  <div class="pill pill--section">Packages</div>

  <div class="package package--silver">
    <div class="pill pill--tier">Silver Package</div>
    <ul class="package__list">
      <li>5 Hours of service</li>
      <li class="sub">(1 hour cocktail, 4 hour reception)</li>
      <li>Illuminated DJ Frontboard</li>
      <li>Standard Lightshow Included</li>
      <li>Professional Corvane Sound System</li>
      <li class="sub">(Wireless Microphones)</li>
    </ul>
    <p class="package__price">Price: $750</p>
  </div>

  <div class="package package--gold">
    <div class="pill pill--tier">Gold Package</div>
    <ul class="package__list">
      <li>5 Hours of service</li>
      <li class="sub">(1 hour cocktail, 4 hour reception)</li>
      <li>Illuminated DJ Frontboard</li>
      <li>Illuminated Luminaro Lighting Fixtures</li>
      <li>Two Intelligent Stratus Truss Towers</li>
      <li>Two 6 ft Stratus Truss Towers</li>
      <li>Professional Corvane Sound System</li>
      <li class="sub">(Wireless Microphones)</li>
    </ul>
    <p class="package__price">Price: $850</p>
  </div>

  <div class="package package--platinum">
    <div class="pill pill--tier">Platinum Package</div>
    <ul class="package__list">
      <li>5 Hours of service</li>
      <li class="sub">(1 hour cocktail, 4 hour reception)</li>
      <li>Illuminated DJ Frontboard</li>
      <li>Two 50" LED Flat Screen TVs</li>
      <li>Custom Made Slide Show Displayed</li>
      <li class="sub">During Reception</li>
      <li>Custom Made GOBO displaying Monogram</li>
      <li>Two Intelligent Luminaro Lighting Fixtures</li>
      <li>Two 6ft Stratus Truss Towers</li>
      <li>Professional Corvane Sound System</li>
      <li class="sub">(Wireless Microphones)</li>
    </ul>
    <p class="package__price">Price: $1050</p>
  </div>

  <p class="reservation">FOR RESERVATION, CALL ON: 555-014-2298</p>
</section>

</body>
</html>
```